Real Estate Agent who sells beach front condos needs a template for a monthly postcard campaign.

Carla Jenrick, Homebroker with Quintavo Real Estate and Development, Licensed in Florida and Alabama, 251-468-3072, carlajenrick.example, carlamjenrick@mailbox.example. Need a postcard template which will allow me to type in recipe instructions and insert a photo of the finished food product. The recipe and photo will change every month, so I need this to be something I can easily change and reorder every month. I sell beach condos primarily. I'd like large photos of the food. Glossy card on both sides.

Target Market(s)

buyers and sellers of homes, condos, lots

Industry/Entity Type

Real Estate Agent

Requirements
Must have
• my contact information, my photo, my company name (Quintavo Real Estate and Development), the Equal Dwelling Logo, the Homebroker Logo, the statement "Contact me for all your Real Estate needs!", a template on the front side that will let me change the photograph at will, and a template on the back side that will let me type words.
Nice to have
• For my contact info and photo to stand out also.

```html
<!DOCTYPE html>
<html lang="en">
<head>
<meta charset="utf-8">
<title>Quintavo Postcard – Carla Jenrick</title>
<link rel="stylesheet" href="https://fonts.googleapis.com/css2?family=Arimo:wght@400;700&family=Lato:wght@400;700&family=Play:wght@400;700&display=swap">
<style>
  :root {
    --stage: #2b2b2b;
    --red: #dc2227;
    --red-dark: #b9171c;
    --pink-light: #f6e6e8;
    --pink: #e7b9bd;
    --ink: #1d1d1d;
    --white: #ffffff;
    --grey-light: #f4f4f4;
    --grey: #cfcfcf;
    --line: #555555;
    --view-a: #9db6cc;
    --view-b: #b8a48e;
    --dish-a: #efe7d8;
    --dish-b: #d99a52;
    --portrait-a: #d9c4a2;
    --portrait-b: #6f655e;
  }
  * { box-sizing: border-box; margin: 0; padding: 0; }
  html, body { width: 875px; height: 1200px; overflow: hidden; }
  body { background: var(--stage); position: relative; font-family: "Arimo", Arial, sans-serif; }

  .card { position: absolute; left: 110px; width: 673px; overflow: hidden; box-shadow: 0 4px 14px rgba(0,0,0,.5); }

  /* ---------- Front ---------- */
  .front { top: 62px; height: 521px;
    background: radial-gradient(ellipse at 40% 40%, var(--pink-light) 0%, var(--pink) 80%, #d9a1a6 100%); }
  .front .title-band { position: absolute; left: 0; top: 31px; width: 673px; height: 69px;
    background: linear-gradient(180deg, var(--red) 0%, var(--red-dark) 100%); }
  .front .headline { position: absolute; left: 22px; top: 35px; font-family: "Play", sans-serif;
    font-weight: 700; font-size: 58px; color: var(--white); letter-spacing: 0; line-height: 62px;
    text-shadow: 1px 2px 2px rgba(0,0,0,.35); }
  .company-box { position: absolute; background: linear-gradient(180deg,#fff 0%,#ececec 100%);
    box-shadow: 0 2px 5px rgba(0,0,0,.35); display: flex; align-items: center; justify-content: center;
    text-align: center; font-family: "Play", sans-serif; font-weight: 700; color: var(--red);
    font-size: 16px; line-height: 22px; }
  .front .company-box { left: 453px; top: 24px; width: 194px; height: 82px; }

  .tag { position: absolute; left: 0; height: 24px; background: var(--red); color: var(--white);
    font-family: "Play", sans-serif; font-weight: 700; font-size: 17px; line-height: 24px; padding-left: 20px; }
  .tag.offer { top: 114px; width: 163px; }
  .tag.contact { top: 414px; width: 125px; }

  .offer-text { position: absolute; left: 20px; top: 143px; width: 333px; font-size: 15px;
    line-height: 18px; text-align: justify; color: var(--ink); }

  .contact-line { position: absolute; left: 14px; font-size: 14px; color: var(--ink);
    display: flex; align-items: center; gap: 7px; }
  .contact-line svg { width: 11px; height: 11px; }
  .contact-line.phone { top: 450px; }
  .contact-line.mail { top: 473px; }

  .front .foot-band { position: absolute; left: 0; bottom: 0; width: 673px; height: 25px;
    background: linear-gradient(180deg, var(--red) 0%, var(--red-dark) 100%); }

  .photo-stack { position: absolute; }
  .photo-stack .under, .photo-stack .frame { position: absolute; inset: 0; background: var(--white);
    box-shadow: 0 2px 6px rgba(0,0,0,.4); }
  .photo-stack .under { transform: rotate(2.5deg); }
  .photo-stack .frame { transform: rotate(-2deg); padding: 6px; }
  .photo-stack .photo { width: 100%; height: 100%; }
  .stack-view { left: 382px; top: 126px; width: 266px; height: 165px; }
  .stack-food { left: 382px; top: 318px; width: 268px; height: 154px; }
  .view-photo { background: linear-gradient(135deg, var(--view-a) 0%, var(--view-b) 100%); }
  .food-photo { background: linear-gradient(135deg, var(--dish-a) 0%, var(--dish-b) 100%); }

  /* ---------- Back ---------- */
  .back { top: 626px; height: 520px; background: var(--white); }
  .back .left-panel { position: absolute; left: 0; top: 0; width: 398px; height: 520px;
    background: linear-gradient(90deg, var(--grey) 0%, var(--grey-light) 50%, var(--white) 100%); }
  .back .title-band { position: absolute; left: 0; top: 29px; width: 673px; height: 57px;
    background: linear-gradient(180deg, var(--red) 0%, var(--red-dark) 100%); }
  .back .section-title { position: absolute; right: 292px; top: 42px; font-family: "Play", sans-serif;
    font-weight: 700; font-size: 27px; color: var(--white); text-shadow: 1px 1px 2px rgba(0,0,0,.35); }
  .back .company-box { left: 445px; top: 11px; width: 190px; height: 80px; }

  .portrait { position: absolute; left: 10px; top: 31px; width: 138px; height: 180px; background: var(--white);
    padding: 7px; transform: rotate(-3deg); box-shadow: 0 2px 6px rgba(0,0,0,.45); }
  .portrait .photo { width: 100%; height: 100%;
    background: linear-gradient(180deg, var(--portrait-a) 0%, var(--portrait-b) 100%); }

  .agent { position: absolute; right: 292px; top: 96px; text-align: right; }
  .agent .name { font-family: "Arimo", sans-serif; font-size: 20px; color: var(--red); letter-spacing: .5px; }
  .agent .role { margin-top: 8px; font-weight: 700; font-size: 12.5px; line-height: 16px; color: var(--ink); }
  .agent .license { margin-top: 5px; font-family: "Lato", sans-serif; font-weight: 700; font-size: 11px; color: var(--red); }
  .agent .detail { margin-top: 9px; font-size: 13px; color: var(--ink); display: flex; justify-content: flex-end;
    align-items: center; gap: 7px; }
  .agent .detail + .detail { margin-top: 8px; }
  .agent .detail svg { width: 11px; height: 11px; }

  .about-text { position: absolute; left: 28px; top: 231px; width: 343px; font-family: "Lato", sans-serif;
    font-size: 13px; line-height: 16px; text-align: justify; color: var(--ink); }
  .about-text p + p { margin-top: 12px; }
  .about-text .cta { margin-top: 10px; font-weight: 700; color: var(--red); text-align: left; }

  .stamp { position: absolute; left: 594px; top: 106px; width: 59px; height: 69px; border: 1px solid var(--ink); }
  .address-line { position: absolute; left: 446px; width: 206px; border-top: 1px solid var(--line); }
  .address-line.one { top: 316px; }
  .address-line.two { top: 361px; }
  .address-line.three { top: 406px; }

  .marks { position: absolute; left: 404px; top: 474px; display: flex; gap: 10px; }
  .mark { display: flex; flex-direction: column; align-items: center; gap: 2px; font-family: "Arimo", sans-serif;
    font-size: 4px; color: var(--ink); }
  .mark .box { width: 22px; height: 22px; background: var(--ink); }
</style>
</head>
<body>

<section class="card front">
  <div class="title-band"></div>
  <h1 class="headline">LOREM IPSUM</h1>
  <div class="company-box">Quintavo Real Estate<br>and Development</div>

  <div class="tag offer">Special Offer</div>
  <p class="offer-text">Lorem ipsum dolor sit amet, consectetuer adiscing elit, sed diam nonummy nibh euismod tincidunt ut laoreet dolore magna aliquam erat volutpat. Ut wisi enim ad minim veniam, quis nostrud exerci tation ullamcorper suscipit lobortis nisl ut aliquip ex ea commodo consequat. Duis autem vel eum iriure dolor in hendrerit in vulputate velit esse molestie cosequat, vel illum dolore eu feugiat. Ut wisi suscipit lobortis nisl ut aliquip tincidunt ut laoreet dolore magna aliquam erat volutpat. Ut wisi enim ad minim veniam, quis nostrud exer. Duis autem vel eum iriure dolor in hendrerit in vulputate elit esse. Lobortis nisl ut aliquip ex ea commodo consequat.</p>

  <div class="tag contact">Contact Us</div>
  <div class="contact-line phone">
    <svg viewBox="0 0 12 12"><path d="M2.5 1 L4.5 1 L5.2 3.6 L3.9 4.6 Q5 7 7.4 8.1 L8.4 6.8 L11 7.5 L11 9.5 Q11 11 9.5 11 Q1 10.5 1 2.5 Q1 1 2.5 1Z" fill="#dc2227"/></svg>
    <span>251-468-3072</span>
  </div>
  <div class="contact-line mail">
    <svg viewBox="0 0 12 12"><rect x="0.5" y="2" width="11" height="8" fill="#dc2227"/><path d="M0.5 2 L6 6.5 L11.5 2" stroke="#fff" stroke-width="1" fill="none"/></svg>
    <span>carlamjenrick@mailbox.example.</span>
  </div>

  <div class="photo-stack stack-view">
    <div class="under"></div>
    <div class="frame"><div class="photo view-photo" role="img" aria-label="Photo of a beachfront condo view"></div></div>
  </div>
  <div class="photo-stack stack-food">
    <div class="under"></div>
    <div class="frame"><div class="photo food-photo" role="img" aria-label="Photo of this month's finished recipe dish"></div></div>
  </div>

  <div class="foot-band"></div>
</section>

<section class="card back">
  <div class="left-panel"></div>
  <div class="title-band"></div>
  <h2 class="section-title">ABOUT ME</h2>
  <div class="company-box">Quintavo Real Estate<br>and Development</div>

  <div class="portrait"><div class="photo" role="img" aria-label="Portrait photo of agent Carla Jenrick"></div></div>

  <div class="agent">
    <div class="name">CARLA JENRICK</div>
    <div class="role">Homebroker with Quintavo Real Estate<br>and Development,</div>
    <div class="license">Licensed in Florida and Alabama,</div>
    <div class="detail"><span>251-468-3072</span>
      <svg viewBox="0 0 12 12"><path d="M2.5 1 L4.5 1 L5.2 3.6 L3.9 4.6 Q5 7 7.4 8.1 L8.4 6.8 L11 7.5 L11 9.5 Q11 11 9.5 11 Q1 10.5 1 2.5 Q1 1 2.5 1Z" fill="#dc2227"/></svg></div>
    <div class="detail"><span>carlamjenrick@mailbox.example</span>
      <svg viewBox="0 0 12 12"><rect x="0.5" y="2" width="11" height="8" fill="#dc2227"/><path d="M0.5 2 L6 6.5 L11.5 2" stroke="#fff" stroke-width="1" fill="none"/></svg></div>
  </div>

  <div class="about-text">
    <p>Lorem ipsum dolor sit amet, consectetuer adipiscing elit. Aenean commodo ligula eget dolor. Aenean massa. Cum sociis natoque penatibus et magnis dis parturient montes.</p>
    <p>Nascetur ridiculus mus. Donec quam felis, ultricies nec, pellentesque eu, pretium quis, sem. Nulla conhhp sequat massa quis enim. Donec pede justo, fringilla vel, aliquet nec.</p>
    <p>Vulputate eget, arcu. In enim justo, rhoncus ut, imperdiet a, venenatis vitae, justo. Nullam dictum felis eu pede mollis pretium. Integer tincidunt. Cras dapibus. Vivamus elemen&shy;tum semper nisi. Aenean</p>
    <p>Aenean vulputate eleifend tellus. Aenean leo ligula, vitae porttitor eu, consequat vitae, eleifend ac, enim. Aliquam lorem ante, dapibus in, viverra quis, feugiat a, tellus. Phaha sellus viverra nulla ut metus varius laoreet.</p>
    <p class="cta">Contact me for all your Real Estate needs!</p>
  </div>

  <div class="stamp"></div>
  <div class="address-line one"></div>
  <div class="address-line two"></div>
  <div class="address-line three"></div>

  <div class="marks">
    <div class="mark"><span class="box"></span><span>Equal Dwelling</span></div>
    <div class="mark"><span class="box"></span><span>Homebroker</span></div>
  </div>
</section>

</body>
</html>
```